Bright Harbor Painting and Remodeling needs a business card

Business card should have company logo. I will upload two different logos and let me see which one is a better design for the business card.

Name of company: Bright Harbor Painting and Remodeling
Address: 4826 NW 61st st Suite 214
Miami, FL 33172

local phone: (305) 555-0143
toll free (855) 555-0176
fax (866) 555-0128

email: darla@brightharborcoats.example

not sure if i should include social media links or names on the business card.

company does interior and exterior painting, pressure washing, wall paper removal, drywall and stucco repair, staining,

We give free estimates.

I want a two sided business card.

Not sure if all this information is necessary for the business card. Designer can pick out whatever information they deem is important for a consumer to see on the business card.

Anticipating on the business card to be printed on nice quality.

I will upload an image of one of the logos on a type of business card surface. That idea can be used as well. Be creative. Business card should be professional but very nice and eye catching.

remove drywall and stucco repair and replace with tile installation

Industry/Entity Type

Business

Contact Information for Business Card

Miami, FL 33172

toll free (855) 555-0176
fax (866) 555-0128

company does interior and exterior painting, pressure washing, wall paper removal, drywall and stucco repair, staining, tile removal, *specializing in vinyl floor removal

free estimates.

Requirements
Must have
• Profesional font

```html
<!DOCTYPE html>
<html lang="en">
<head>
<meta charset="UTF-8">
<title>Bright Harbor Painting and Remodeling – Business Card</title>
<link href="https://fonts.googleapis.com/css2?family=Montserrat:wght@500;600;700&family=PT+Sans+Narrow:wght@400;700&display=swap" rel="stylesheet">
<style>
  :root {
    --page: #e9e8ec;
    --card-dark: #2f2b2c;
    --card-light: #ffffff;
    --purple: #9a6fd1;
    --purple-deep: #8a5cc6;
    --ink: #1d1b1e;
    --yellow: #f6d35a;
    --orange: #f7a85b;
    --pink: #ef6d86;
    --white: #ffffff;
  }
  * { margin: 0; padding: 0; box-sizing: border-box; }
  html, body { width: 1200px; height: 900px; overflow: hidden; }
  body {
    background: var(--page);
    position: relative;
    font-family: "Montserrat", Arial, sans-serif;
  }
  .card {
    position: absolute;
    width: 700px;
    height: 400px;
    overflow: hidden;
    box-shadow: 0 10px 30px rgba(0,0,0,0.18);
  }
  .card--back { left: 70px; top: 45px; background: var(--card-dark); }
  .card--front { left: 430px; top: 455px; background: var(--card-light); }

  .brand {
    position: absolute;
    display: flex;
    align-items: center;
    gap: 12px;
    font-family: "Montserrat", Arial, sans-serif;
    font-weight: 700;
    text-transform: uppercase;
    letter-spacing: 0.04em;
    line-height: 1.15;
  }
  .brand__dot { border-radius: 50%; flex: none; }
  .card--back .brand { left: 200px; top: 70px; color: var(--white); font-size: 24px; }
  .card--back .brand__dot { width: 46px; height: 46px; background: var(--yellow); }
  .card--front .brand { right: 60px; top: 45px; color: var(--ink); font-size: 17px; }
  .card--front .brand__dot { width: 34px; height: 34px; background: var(--yellow); }
  .brand__sub { display: block; font-size: 0.62em; letter-spacing: 0.14em; }

  .social {
    position: absolute;
    width: 26px; height: 26px;
    border-radius: 50%;
    background: var(--white);
  }
  .social--a { right: 110px; top: 50px; }
  .social--b { right: 50px; top: 50px; }
  .social--c { left: 40px; top: 262px; }
  .social--d { left: 100px; top: 262px; }

  .services {
    position: absolute;
    left: 40px; right: 40px; top: 205px;
    font-family: "PT Sans Narrow", Arial, sans-serif;
    font-weight: 700;
    font-size: 19px;
    color: var(--purple);
    text-transform: uppercase;
    letter-spacing: 0.03em;
    text-align: center;
    line-height: 1.35;
  }
  .services__sep { color: var(--yellow); padding: 0 4px; }
  .services__note { color: var(--yellow); padding: 0 4px; }
  .services__list { position: absolute; left: 150px; right: 20px; top: 300px; }

  .bar { position: absolute; height: 12px; }
  .bar--top { right: 0; top: 168px; width: 130px; background: linear-gradient(90deg, var(--purple), var(--pink), var(--orange)); }
  .bar--bottom { left: 0; bottom: 55px; width: 130px; background: linear-gradient(90deg, var(--orange), var(--pink), var(--purple)); }

  .rule {
    position: absolute;
    left: 0; top: 205px;
    width: 360px; height: 10px;
    background: linear-gradient(90deg, var(--yellow), var(--orange), var(--pink), var(--purple));
  }
  .contact {
    position: absolute;
    left: 385px; top: 150px;
    color: var(--ink);
  }
  .contact__name { font-size: 25px; font-weight: 700; color: var(--purple); text-transform: uppercase; letter-spacing: 0.01em; }
  .contact__title { font-size: 15px; font-weight: 600; margin-bottom: 14px; }
  .contact__address { font-size: 15px; font-weight: 600; color: var(--purple); line-height: 1.25; margin-bottom: 14px; }
  .contact__list { list-style: none; font-size: 15px; font-weight: 500; line-height: 1.5; }
  .contact__list li { display: flex; align-items: center; gap: 10px; }
  .contact__icon { width: 14px; height: 14px; flex: none; }
</style>
</head>
<body>

<section class="card card--back" aria-label="Back of business card">
  <div class="brand">
    <span class="brand__dot"></span>
    <span>Bright Harbor<span class="brand__sub">Painting and Remodeling</span></span>
  </div>
  <span class="social social--a"></span>
  <span class="social social--b"></span>
  <span class="bar bar--top"></span>

  <p class="services">
    Interior &amp; Exterior Painting<span class="services__sep">|</span>Pressure Washing<span class="services__sep">|</span>Wall Paper Removal<br>
    Tile Installation<span class="services__sep">|</span>Staining<span class="services__sep">|</span>Tile Removal<br>
    <span class="services__note">*</span>Specializing in Vinyl Floor Removal<span class="services__note">*</span>Free Estimates
  </p>

  <span class="social social--c"></span>
  <span class="social social--d"></span>
  <span class="bar bar--bottom"></span>
</section>

<section class="card card--front" aria-label="Front of business card">
  <div class="brand">
    <span class="brand__dot"></span>
    <span>Bright Harbor<span class="brand__sub">Painting and Remodeling</span></span>
  </div>

  <span class="rule"></span>

  <div class="contact">
    <h1 class="contact__name">Darla Whitford</h1>
    <p class="contact__title">Managing Director</p>
    <p class="contact__address">4826 NW 61st st Suite 214<br>Miami, FL 33172</p>
    <ul class="contact__list">
      <li>
        <svg class="contact__icon" viewBox="0 0 16 16" aria-hidden="true"><path d="M2 5c0-1.5 2.5-3 6-3s6 1.5 6 3l-3 1-1-2H6L5 6 2 5zM4 8h8l2 6H2z" fill="var(--purple-deep)"/></svg>
        (305) 555-0143
      </li>
      <li>
        <svg class="contact__icon" viewBox="0 0 16 16" aria-hidden="true"><path d="M3 1l3 1 1 4-2 1c1 2 2 3 4 4l1-2 4 1 1 3c-1 2-3 2-5 1C6 12 4 10 2 7 1 5 1 3 3 1z" fill="var(--purple-deep)"/></svg>
        (855) 555-0176
      </li>
      <li>
        <svg class="contact__icon" viewBox="0 0 16 16" aria-hidden="true"><rect x="4" y="1" width="8" height="5" fill="none" stroke="var(--purple-deep)" stroke-width="1.5"/><rect x="1" y="6" width="14" height="6" rx="1" fill="var(--purple-deep)"/><rect x="4" y="10" width="8" height="5" fill="#fff" stroke="var(--purple-deep)" stroke-width="1.5"/></svg>
        (866) 555-0128
      </li>
      <li>
        <svg class="contact__icon" viewBox="0 0 16 16" aria-hidden="true"><rect x="1" y="3" width="14" height="10" fill="none" stroke="var(--purple-deep)" stroke-width="1.5"/><path d="M1 3l7 6 7-6" fill="none" stroke="var(--purple-deep)" stroke-width="1.5"/></svg>
        darla@brightharborcoats.example
      </li>
    </ul>
  </div>
</section>

</body>
</html>
```